Neudesign von Visitenkarten und Briefpapier für Eventmanager
Zielgruppe
Als Eventmanager bin ich seit mehr als 15 Jahren in verschiedenen Tätigkeitsfeldern und Veranstaltungsbereichen tätig.
Wechselnde Auftraggeber, Arbeitsfelder und Themen prägen meinen beruflichen Alltag.
Die Bandbreite der Tätigkeiten reicht von Organisation und Durchführung über Konzeption und Planung bis zu Management und Beratung.
Schwerpunkt und Gemeinsamkeit ist eine planerische Tätigkeit mit Umsetzung vor Ort.
Das Wort Produktionsbüro spielt in meinen Tätigkeiten immer eine große Rolle. Produktionsbüros sind die zentrale Schaltstelle bei Veranstaltungen.
Die Domain www.taktwerkstatt.de ist meine. (es gibt keinen Internetauftritt)
Bereiche: Corporate Events, Entertainment und Musik-Tourneen, Ausstellungen
international tätig
Auftraggeber sind sowohl Endkunden als auch Agenturen aus den verschiedenen Bereichen. (Eventagenturen, Tournee- und Konzertveranstalter, internationale Ausstellungsgesellschaften)
Aufgabenstellung
Entwicklung einer Wort-/Bildmarke
Stichworte: sachlich, schnörkellos, klar, nicht verspielt, zeitlos
Gestaltung von Visitenkarten und Briefpapier
Das Design muß sich ändern lassen (z.B. Umzug) und rein digital verwendbar sein – kein Druck von Briefpapier, sondern Korrespondenz lediglich digital aus MS Word/Word für MAC.
Mögliche Ansätze:
„Dornhagen“ als Personen- und Markennamen hervorheben
„stage bureau“ als überspannenden Tätigkeitsbegriff und -namen hervorheben
Das Design sollte s/w (Grautöne) oder farblich dezent sein (1 Farbe + Grau).
Im Anhang mein derzeitiges Briefpapier und die Visitenkarte. Alle diese Information sollen auch zukünftig Platz finden.

```html
<!DOCTYPE html>
<html lang="de">
<head>
<meta charset="utf-8">
<title>Dornhagen stage bureau – Visitenkarten</title>
<link rel="stylesheet" href="https://fonts.googleapis.com/css2?family=Inconsolata:wght@400&display=swap">
<style>
  :root {
    --page: #efefef;
    --paper: #ffffff;
    --charcoal: #3d3d3f;
    --accent: #e8692c;
    --ink: #333335;
    --ink-soft: #59595c;
    --ink-light: #d9d9d9;
  }
  * { box-sizing: border-box; margin: 0; padding: 0; }
  html, body { width: 1200px; height: 900px; overflow: hidden; }
  body {
    background: var(--page);
    display: grid;
    grid-template-columns: repeat(2, 530px);
    grid-template-rows: repeat(2, 340px);
    gap: 60px;
    padding: 80px 40px;
    font-family: "Inconsolata", monospace;
  }
  .card {
    position: relative;
    width: 530px;
    height: 340px;
    background: var(--paper);
    color: var(--ink);
  }
  .card--dark { background: var(--charcoal); color: var(--ink-light); }

  .brand {
    position: absolute;
    left: 32px;
    top: 36px;
    width: 440px;
  }
  .brand__name {
    font-size: 72px;
    line-height: 1;
    font-weight: 400;
    color: var(--accent);
  }
  .brand__tagline {
    font-size: 23px;
    letter-spacing: 2px;
    text-align: right;
    margin-top: 18px;
    color: var(--ink-soft);
  }
  .card--dark .brand__tagline { color: var(--ink-light); }

  .services {
    position: absolute;
    left: 12px;
    top: 222px;
    display: grid;
    grid-template-columns: 150px 30px 116px 36px 100px;
    row-gap: 16px;
    font-size: 13px;
    letter-spacing: 0.4px;
    line-height: 16px;
    text-align: center;
    white-space: nowrap;
  }

  .contact {
    position: absolute;
    left: 19px;
    top: 252px;
    display: grid;
    grid-template-columns: 193px auto;
    font-size: 15px;
    line-height: 18px;
    letter-spacing: 0.4px;
    white-space: nowrap;
  }
</style>
</head>
<body>

  <section class="card card--front">
    <div class="brand">
      <div class="brand__name">dornhagen</div>
      <div class="brand__tagline">stage bureau</div>
    </div>
    <div class="services">
      <span>konzept</span><span>||</span><span>organisation</span><span>||</span><span>management</span>
      <span>corporate events</span><span>||</span><span>entertainment</span><span>||</span><span>ausstellung</span>
    </div>
  </section>

  <section class="card card--front card--dark">
    <div class="brand">
      <div class="brand__name">dornhagen</div>
      <div class="brand__tagline">stage bureau</div>
    </div>
    <div class="services">
      <span>konzept</span><span>||</span><span>organisation</span><span>||</span><span>management</span>
      <span>corporate events</span><span>||</span><span>entertainment</span><span>||</span><span>ausstellung</span>
    </div>
  </section>

  <section class="card card--back card--dark">
    <div class="brand">
      <div class="brand__name">dornhagen</div>
      <div class="brand__tagline">stage bureau</div>
    </div>
    <div class="contact">
      <div class="contact__address">birkenallee 3c<br>51789 lindlar</div>
      <div class="contact__reach">dornhagen@taktwerkstatt.de<br>+49 (0) 170 555 123 45</div>
    </div>
  </section>

  <section class="card card--back">
    <div class="brand">
      <div class="brand__name">dornhagen</div>
      <div class="brand__tagline">stage bureau</div>
    </div>
    <div class="contact">
      <div class="contact__address">birkenallee 3c<br>51789 lindlar</div>
      <div class="contact__reach">dornhagen@taktwerkstatt.de<br>+49 (0) 170 555 123 45</div>
    </div>
  </section>

</body>
</html>
```